'Lanterns' CD cover project

I am recording a new album 'Lanterns' and need a CD cover design. No design specs, but I want something simple and classy. My name (Maren Tolvey) does not necessarily have to appear on the cover, and it does not have to relate to my previous 11 albums. I have posted some of my own ideas on Chatterly.

Target Market(s)

I have an established 50s+ fan base, but am seeking to appeal to a younger more modern audience.

Font styles to use
Other font styles liked:
• Yu Gothic Light but open to suggestions.

Colors

Designer to choose colors to be used in the design.

Requirements
Must have
• Simple, clean, classy, Im open to a photo image or simply a graphic design.
Nice to have
• Modern (pastel?) colors.. if pastels are modern?!
Should not have
• Nothing 'In Yer Face'. Prefer sublte, nuance, classy, tasteful, clean lines, unusual font.

```html
<!DOCTYPE html>
<html lang="en">
<head>
<meta charset="utf-8">
<title>Lanterns</title>
<link href="https://fonts.googleapis.com/css2?family=Jost:wght@300&display=swap" rel="stylesheet">
<style>
  :root {
    --page: #ffffff;
    --stone-dark: #4a4034;
    --stone-mid: #7d7160;
    --field-green: #8fa83a;
    --haze: #e6ead2;
    --veil: rgba(255, 255, 255, 0.32);
    --title: #ffffff;
  }
  html, body {
    margin: 0;
    padding: 0;
    width: 1200px;
    height: 1200px;
    overflow: hidden;
    background: var(--page);
  }
  .cover {
    position: relative;
    width: 1200px;
    height: 1200px;
    background: var(--page);
  }
  .cover-photo {
    position: absolute;
    left: 150px;
    top: 106px;
    width: 904px;
    height: 830px;
    background:
      radial-gradient(ellipse 42% 38% at 50% 52%, var(--haze) 0%, var(--field-green) 45%, rgba(143,168,58,0) 75%),
      radial-gradient(ellipse 70% 70% at 50% 50%, var(--stone-mid) 0%, var(--stone-dark) 100%);
  }
  .title-band {
    position: absolute;
    left: 368px;
    top: 106px;
    width: 442px;
    height: 830px;
    background: var(--veil);
  }
  .album-title {
    position: absolute;
    left: 368px;
    width: 442px;
    top: 782px;
    margin: 0;
    text-align: center;
    font-family: "Jost", sans-serif;
    font-weight: 300;
    font-size: 84px;
    line-height: 1;
    letter-spacing: 0;
    color: var(--title);
  }
</style>
</head>
<body>
  <main class="cover">
    <div class="cover-photo" role="img" aria-label="Upward view from a stone courtyard lined with windows, opening onto a green rice field with a winding river beneath a hazy sky"></div>
    <div class="title-band"></div>
    <h1 class="album-title">LANTERNS</h1>
  </main>
</body>
</html>
```